Business Card for Graphic Design Firm

This project is for a new graphic design firm based in New Jersey called Velmoth. We outsource graphic design and marketing jobs. We want to communicate that this is a professional company but it as well creative and artistic. This card may be used as a horizontal double sided paper card or a vertical single sided translucent card so feel free to submit designs in whichever format or both.
Updates

Reason: Extending the deadline because I'm not exactly satisfied with the designs so far.

Please view the updated project brief

Target Market(s)

Adults aged 25-60

Industry/Entity Type

Graphic Design

Font styles to use
Serif
Sans Serif

Requirements
Nice to have
• Maybe a triangular pattern around the edges similar to our logo

```html
<!DOCTYPE html>
<html lang="en">
<head>
<meta charset="utf-8">
<title>Velmoth — Business Card</title>
<link rel="stylesheet" href="https://fonts.googleapis.com/css2?family=Questrial&display=swap">
<style>
  :root {
    --backdrop: #2a2a2c;
    --card-frost: #b7babd;
    --card-edge: #c9ccce;
    --ink-grey: #85898c;
    --accent-teal: #1fa3b3;
    --accent-teal-deep: #1b7f96;
    --accent-sky: #6cc3df;
    --accent-yellow: #f3b424;
    --accent-orange: #ec8a2a;
  }
  html, body {
    margin: 0;
    padding: 0;
    width: 1200px;
    height: 811px;
    overflow: hidden;
    background: var(--backdrop);
  }
  .canvas {
    position: relative;
    width: 1200px;
    height: 811px;
    font-family: "Questrial", sans-serif;
  }
  .card {
    position: absolute;
    left: 410px;
    top: 73px;
    width: 380px;
    height: 665px;
    border-radius: 18px;
    background: var(--card-frost);
    box-shadow: inset 0 0 0 2px var(--card-edge);
    overflow: hidden;
  }
  .brand {
    position: absolute;
    left: 40px;
    top: 48px;
    display: flex;
    align-items: center;
    gap: 12px;
  }
  .brand-square {
    width: 20px;
    height: 20px;
    background: var(--ink-grey);
  }
  .brand-name {
    font-size: 26px;
    letter-spacing: 5px;
    color: var(--ink-grey);
    text-transform: uppercase;
  }
  .contact {
    position: absolute;
    left: 40px;
    top: 300px;
  }
  .contact-name {
    margin: 0 0 12px;
    font-size: 24px;
    font-weight: 400;
    letter-spacing: 1px;
    color: var(--accent-teal);
    text-transform: uppercase;
  }
  .contact-line {
    margin: 0 0 4px;
    font-size: 15px;
    color: var(--ink-grey);
  }
  .contact-line.web {
    color: var(--accent-teal);
  }
  .pattern-area {
    position: absolute;
    left: 0;
    bottom: 0;
    width: 380px;
    height: 230px;
    display: block;
  }
</style>
</head>
<body>
<div class="canvas">
  <section class="card">
    <div class="brand">
      <span class="brand-square"></span>
      <span class="brand-name">Velmoth</span>
    </div>

    <div class="contact">
      <h1 class="contact-name">Dorian Vale</h1>
      <p class="contact-line">041 672 358</p>
      <p class="contact-line">dorian@velmoth.com</p>
      <p class="contact-line web">www.velmoth.com</p>
    </div>

    <svg class="pattern-area" viewBox="0 0 380 230" role="img" aria-label="Geometric triangle pattern in teal, sky blue, yellow and orange">
      <defs>
        <linearGradient id="pattern-tones" x1="0" y1="0" x2="1" y2="0">
          <stop offset="0" stop-color="var(--accent-teal-deep)"/>
          <stop offset="0.35" stop-color="var(--accent-teal)"/>
          <stop offset="0.5" stop-color="var(--accent-sky)"/>
          <stop offset="0.7" stop-color="var(--accent-yellow)"/>
          <stop offset="1" stop-color="var(--accent-orange)"/>
        </linearGradient>
      </defs>
      <rect x="0" y="0" width="380" height="230" fill="url(#pattern-tones)"/>
    </svg>
  </section>
</div>
</body>
</html>
```